Website for Company that serves and supports Investment Banks

We are seeking to have a six page website that provides a basic description of our company's services. Our company provides Financial Models and Investment Memos on an outsourced basis to Small Investment Banks and Investment firms. We do not require a shopping cart. We already have a logo attached.

Target Market(s)

Small, regional investment banks. Small private equity firms.

Industry/Entity Type

Finance And Accounting

Coding

Coded - Design and coding required

Number of Pages Required

5+ page

Requirements
Nice to have
• Please use the logo design to drive how you design the layout for the website

```html
<!DOCTYPE html>
<html lang="en">
<head>
<meta charset="utf-8">
<title>LedgerPeakAdvisory.com</title>
<link href="https://fonts.googleapis.com/css2?family=Open+Sans:wght@300;400;600;700&display=swap" rel="stylesheet">
<style>
:root{
  --navy:#0d4a7a;
  --navy-dark:#0a3a61;
  --blue:#2f78b7;
  --sky:#dff1f8;
  --orange:#f28a22;
  --text:#555b62;
  --heading:#2b3a4a;
  --white:#ffffff;
  --footer:#0a2f4f;
}
*{margin:0;padding:0;box-sizing:border-box}
html,body{width:1200px;height:3568px;overflow:hidden}
body{font-family:"Open Sans",Arial,sans-serif;color:var(--text);background:var(--white);position:relative}
section,header,footer,nav{position:absolute;left:0;width:1200px}
.media{position:absolute}

/* header */
.topbar{top:0;height:44px;background:var(--white)}
.brand{position:absolute;left:64px;top:12px;display:flex;align-items:center;gap:8px;font-weight:700;font-size:13px;color:var(--navy)}
.brand-dot{width:18px;height:18px;border-radius:50%;background:var(--navy)}
.top-contact{position:absolute;right:40px;top:14px;display:flex;gap:26px;font-size:12px;color:var(--heading)}
.top-contact span{display:flex;align-items:center;gap:6px}
.mainnav{top:44px;height:34px;background:var(--navy);display:flex;align-items:center;justify-content:flex-start;gap:18px;padding-left:100px;z-index:2}
.mainnav a{color:var(--white);font-size:13px;text-decoration:none;padding:6px 4px;white-space:nowrap}
.mainnav a.active{border-bottom:2px solid var(--orange)}

/* hero */
.hero{top:78px;height:642px;background:linear-gradient(90deg,#cfe0ec 0%,#e8f1f7 50%,#f4f8fb 100%)}
.hero .media{left:0;top:0;width:560px;height:642px;background:linear-gradient(160deg,#b8cbd9,#d9e3ea 55%,#c9d6df)}
.hero-copy{position:absolute;left:600px;top:236px;width:520px}
.hero-copy h1{font-weight:300;font-size:42px;line-height:52px;color:var(--blue)}
.hero-copy p{margin-top:16px;font-size:13px;line-height:20px}
.btn{display:inline-block;background:var(--navy);color:var(--white);font-size:13px;font-weight:600;padding:10px 32px;margin-top:22px;text-decoration:none}

/* shared */
.sec-title{font-weight:400;font-size:32px;color:var(--heading)}
.sec-title::after{content:"";display:block;width:60px;height:3px;background:var(--orange);margin-top:8px}
.bullets{list-style:none;margin-top:22px}
.bullets li{position:relative;font-size:13px;line-height:20px;padding:9px 14px 9px 30px;border-bottom:1px solid #e3e7ea}
.bullets li::before{content:"";position:absolute;left:12px;top:16px;width:7px;height:7px;border-radius:50%;background:var(--orange)}
.bullets li.highlight{background:var(--orange);color:var(--white);border:none}
.bullets li.highlight::before{background:var(--white)}

/* about */
.about{top:720px;height:410px;background:var(--white)}
.about-copy{position:absolute;left:80px;top:50px;width:580px}
.about .media{left:720px;top:60px;width:400px;height:230px;background:linear-gradient(135deg,#dfe8ef,#b9cbd9);box-shadow:0 6px 16px rgba(0,0,0,.15)}

/* leadership */
.leadership{top:1130px;height:490px;background:linear-gradient(180deg,#eaf6fb,var(--sky))}
.leadership .media{left:80px;top:50px;width:380px;height:300px;background:linear-gradient(140deg,#c9d6e0,#e9eef2 60%,#b9c8d4);box-shadow:0 6px 16px rgba(0,0,0,.12)}
.lead-copy{position:absolute;left:520px;top:90px;width:600px}
.lead-copy p{margin-top:22px;font-size:13px;line-height:21px}

/* products */
.products{top:1620px;height:380px;background:var(--white);text-align:center}
.products .sec-title{margin-top:80px;display:inline-block}
.products .sec-title::after{margin:8px auto 0}
.product-grid{display:flex;justify-content:center;gap:120px;margin-top:44px}
.product{width:160px;display:flex;flex-direction:column;align-items:center}
.product-icon{width:110px;height:110px;background:var(--navy);display:flex;align-items:center;justify-content:center;box-shadow:0 4px 10px rgba(0,0,0,.2)}
.product span{margin-top:16px;font-size:14px;color:var(--heading)}

/* why */
.why{top:2000px;height:440px;background:var(--navy)}
.why-copy{position:absolute;left:80px;top:44px;width:580px;color:var(--white)}
.why-copy .sec-title{color:var(--white);line-height:40px}
.why .bullets li{border-bottom:1px solid rgba(255,255,255,.2);color:var(--white)}
.why .bullets li.highlight{background:var(--white);color:var(--navy)}
.why .bullets li.highlight::before{background:var(--orange)}
.why .media{left:720px;top:60px;width:400px;height:310px;background:linear-gradient(150deg,#6b5a4a,#b59a7e 55%,#8a7260);border:6px solid var(--white)}

/* intake */
.intake{top:2440px;height:500px;background:var(--white)}
.intake .media{left:80px;top:70px;width:400px;height:360px;background:linear-gradient(150deg,#e7ebee,#cfd8df);box-shadow:0 6px 16px rgba(0,0,0,.12)}
.intake-copy{position:absolute;left:540px;top:60px;width:580px}
.intake-copy .sec-title{line-height:40px}

/* contact */
.contact{top:2940px;height:260px;background:var(--navy);color:var(--white)}
.contact h2{text-align:center;font-weight:400;font-size:26px;letter-spacing:1px;margin-top:50px}
.contact-grid{display:flex;justify-content:space-between;padding:0 120px;margin-top:36px}
.contact-item{display:flex;gap:14px;width:300px}
.contact-item h3{font-size:14px;font-weight:600}
.contact-item p{font-size:12px;line-height:18px;margin-top:6px;opacity:.9}

/* map */
.map{top:3200px;height:320px;background:linear-gradient(135deg,#e4e9ed,#d5dde3 50%,#e7ecef)}

/* footer */
.site-footer{top:3520px;height:48px;background:var(--footer);color:#c7d3dd;font-size:12px;display:flex;align-items:center;justify-content:center}
</style>
</head>
<body>

<header class="topbar">
  <div class="brand"><span class="brand-dot"></span>LedgerPeakAdvisory.com</div>
  <div class="top-contact">
    <span><svg width="12" height="12" viewBox="0 0 24 24"><path fill="#0d4a7a" d="M6.6 10.8a15 15 0 006.6 6.6l2.2-2.2a1 1 0 011-.25 11.4 11.4 0 003.6.6 1 1 0 011 1V20a1 1 0 01-1 1A17 17 0 013 4a1 1 0 011-1h3.5a1 1 0 011 1 11.4 11.4 0 00.6 3.6 1 1 0 01-.25 1z"/></svg>800-555-0142</span>
    <span><svg width="13" height="11" viewBox="0 0 24 18"><rect x="1" y="1" width="22" height="16" fill="none" stroke="#0d4a7a" stroke-width="2"/><path d="M1 1l11 9 11-9" fill="none" stroke="#0d4a7a" stroke-width="2"/></svg>info@ledgerpeakadvisory.com</span>
  </div>
</header>

<nav class="mainnav">
  <a class="active" href="#about">About Us</a>
  <a href="#leadership">Company Leadership</a>
  <a href="#products">Product Offering</a>
  <a href="#why">Why Hire LedgerPeakAdvisory.com?</a>
  <a href="#intake">How Our Client Intake Process Works?</a>
  <a href="#contact">Contact Us</a>
</nav>

<section class="hero">
  <div class="media" role="img" aria-label="Photo of two smiling professionals working together at a desk"></div>
  <div class="hero-copy">
    <h1>Lorem Ipsum is simply<br>dummy text</h1>
    <p>Lorem Ipsum is simply dummy text of the printing and typesetting industry. Lorem Ipsum has been the industry's standard dummy text ever since the 1500s.</p>
    <a class="btn" href="#about">Read More</a>
  </div>
</section>

<section class="about" id="about">
  <div class="about-copy">
    <h2 class="sec-title">About Us</h2>
    <ul class="bullets">
      <li class="highlight">LedgerPeakAdvisory.com functions as an outsourced financial analyst partner for smaller regional investment banks, private equity firms and business brokers.</li>
      <li>We focus exclusively on lower middle market clients.</li>
      <li>We deliver Financial Models and Investment Memos, two of the most important deal support tools for executing private equity and investment banking transactions.</li>
      <li>LedgerPeakAdvisory.com specializes in delivering robust LBO, Growth Equity, Recap and Merger models.</li>
    </ul>
  </div>
  <div class="media" role="img" aria-label="Photo of financial charts and reports on a desk"></div>
</section>

<section class="leadership" id="leadership">
  <div class="media" role="img" aria-label="Photo of a business team meeting around a laptop"></div>
  <div class="lead-copy">
    <h2 class="sec-title">Company Leadership</h2>
    <p>Daniel Reeve is Managing Partner of LedgerPeakAdvisory.com. He has over 10 years of experience producing financial models and drafting investment memos. He previously worked as an investment banking Financial Analyst in Harbor Crest Partners' Corporate Finance Department. He also previously worked as a Financial Analyst at Northfield Strategy Group. Daniel has taught in-depth seminars providing transactional deal support to some of the most talented investment bankers, private equity investors and management consultants in the market.</p>
    <a class="btn" href="#products">Read More</a>
  </div>
</section>

<section class="products" id="products">
  <h2 class="sec-title">Product Offering</h2>
  <div class="product-grid">
    <div class="product">
      <div class="product-icon"><svg width="56" height="56" viewBox="0 0 56 56"><path d="M6 50h44M12 44V30M22 44V22M32 44V26M42 44V12" stroke="#fff" stroke-width="5" fill="none"/></svg></div>
      <span>Financial Models</span>
    </div>
    <div class="product">
      <div class="product-icon"><svg width="56" height="56" viewBox="0 0 56 56"><circle cx="28" cy="28" r="20" fill="none" stroke="#fff" stroke-width="4"/><path d="M34 20h-8a4 4 0 000 8h4a4 4 0 010 8h-8M28 14v6M28 36v6" stroke="#fff" stroke-width="3" fill="none"/></svg></div>
      <span>Valuation Models</span>
    </div>
    <div class="product">
      <div class="product-icon"><svg width="56" height="56" viewBox="0 0 56 56"><path d="M14 6h20l10 10v34H14z" fill="none" stroke="#fff" stroke-width="4"/><path d="M20 26h18M20 34h18M20 42h12" stroke="#fff" stroke-width="3"/></svg></div>
      <span>Investment Documents</span>
    </div>
    <div class="product">
      <div class="product-icon"><svg width="56" height="56" viewBox="0 0 56 56"><rect x="8" y="10" width="40" height="36" fill="none" stroke="#fff" stroke-width="4"/><path d="M16 22l5 5 9-9M16 36h24" stroke="#fff" stroke-width="3" fill="none"/></svg></div>
      <span>Deal Support Memos</span>
    </div>
  </div>
</section>

<section class="why" id="why">
  <div class="why-copy">
    <h2 class="sec-title">Why Hire LedgerPeak<br>Advisory.com?</h2>
    <ul class="bullets">
      <li class="highlight">We are much more cost effective than hiring full-time Analyst pool.</li>
      <li>We give You the ability to purchase Financial Models and Investment Memos on a "product by product" on-demand basis with standardized prices.</li>
      <li>Cost of our Financial Models and Investment Memos is less expensive than other outsourced deal providers including investment bankers, attorneys, accountants and industry consultants.</li>
      <li>Cost of our Financial Models and Investment Memos is less expensive than Quality of Earnings Analysis reports provided by accounting firms.</li>
    </ul>
  </div>
  <div class="media" role="img" aria-label="Photo of hands typing on a laptop on a wooden desk"></div>
</section>

<section class="intake" id="intake">
  <div class="media" role="img" aria-label="Photo of a smiling businesswoman in an office"></div>
  <div class="intake-copy">
    <h2 class="sec-title">How Our Client Intake<br>Process Works?</h2>
    <ul class="bullets">
      <li class="highlight">Call or email us a brief two sentence description of your deal project and indicate whether you are interested in our Financial Model or Investment Memo products.</li>
      <li>An LedgerPeakAdvisory.com client service rep will contact you within 24 hours.</li>
      <li>To ensure confidentiality, we will request that you forward a copy of your Non-Disclosure Agreement for our execution.</li>
      <li>In order for us to get our arms around the transaction we will email you a blank Sources &amp; Uses of Funds template. In order for us to get our arms around the transaction we will email you a blank Sources &amp; Uses of Funds.</li>
    </ul>
  </div>
</section>

<section class="contact" id="contact">
  <h2>CONTACT US</h2>
  <div class="contact-grid">
    <div class="contact-item">
      <svg width="26" height="26" viewBox="0 0 24 24"><path fill="#fff" d="M6.6 10.8a15 15 0 006.6 6.6l2.2-2.2a1 1 0 011-.25 11.4 11.4 0 003.6.6 1 1 0 011 1V20a1 1 0 01-1 1A17 17 0 013 4a1 1 0 011-1h3.5a1 1 0 011 1 11.4 11.4 0 00.6 3.6 1 1 0 01-.25 1z"/></svg>
      <div><h3>Phones</h3><p>800-555-0142</p></div>
    </div>
    <div class="contact-item">
      <svg width="22" height="28" viewBox="0 0 22 28"><path fill="#fff" d="M11 0a11 11 0 00-11 11c0 8 11 17 11 17s11-9 11-17A11 11 0 0011 0zm0 15a4 4 0 110-8 4 4 0 010 8z"/></svg>
      <div><h3>Address</h3><p>LedgerPeakAdvisory.com<br>250 Elm Harbor Street<br>Suite 4<br>Riverton, MA 01999</p></div>
    </div>
    <div class="contact-item">
      <svg width="26" height="20" viewBox="0 0 24 18"><rect x="1" y="1" width="22" height="16" fill="none" stroke="#fff" stroke-width="2"/><path d="M1 1l11 9 11-9" fill="none" stroke="#fff" stroke-width="2"/></svg>
      <div><h3>Email</h3><p>info@ledgerpeakadvisory.com</p></div>
    </div>
  </div>
</section>

<section class="map" role="img" aria-label="Street map showing the office location with a red marker"></section>

<footer class="site-footer">Copyright 2017 @ All Rights Reserved</footer>

</body>
</html>
```